New webpage design for Talvora.se, participant management system informationpage.

Project Brief: New Website Design for Talvora.se (Participant Management System)
About Talvora.se:
Talvora.se is an established participant management system used by organizations and course providers in Sweden to handle event and course registrations. Our website’s primary audience is course providers, event organizers, and potential users seeking efficient management tools.
Project Goal:
We are launching a new public-facing website for Talvora.se, which will present information about our system, features, FAQ, pricing, news, testimonials, and more. The new site will be built in Umbraco CMS and should follow our visual identity as described in the attached graphic manual.
Deliverables:
We need complete, modern, and responsive page designs (desktop and mobile) for the following pages:
- Home page (landing page)
- Features page
- FAQ page
- About Us page
- Contact Us / Book a Demo page
- Pricing page
- Testimonials page
- News / Blog page
Design Guidelines:
- Please use the attached Plomvik graphic manual for guidance (Plomvik is a sister project; use the same branding).
- The Talvora.se logo is attached and must be included.
- Please use the blue color palette variant from the guide.
- Typography and graphic elements should be consistent with the manual.
- Designs must be suitable for implementation in Umbraco CMS (avoid overly complex layouts or animations that might be difficult to develop).
- All designs should be responsive and work well on desktop, tablet, and mobile.
- Final deliverables should be provided in Figma or Adobe XD (preferably Figma).
What We Like:
- Clean, modern, Scandinavian style.
- Clear navigation and strong hierarchy.
- Readable, accessible layouts.
What to Avoid:
- Overly playful or cartoonish elements.
- Too much clutter or excessive graphical elements.
- Dark color schemes (please focus on blue/light).
References:
- Our current site: https://talvora-demo.se
- Graphic manual (see attachment)
- Talvora logo (see attachment)
Additional Notes:
- The new design should improve clarity, usability, and visual appeal compared to our current site.
- Feel free to suggest visual improvements, but remain consistent with our brand guidelines.
Other font styles liked:
- Orev and Cabin. See attached font files

```html
<!DOCTYPE html>
<html lang="en">
<head>
<meta charset="utf-8">
<title>Talvora – Participant management</title>
<link href="https://fonts.googleapis.com/css2?family=Oxanium:wght@500;600;700&family=Cabin:wght@400;500;600;700&display=swap" rel="stylesheet">
<style>
:root{
  --blue:#2f62e6;
  --blue-deep:#2654d4;
  --green:#17b07b;
  --green-deep:#0f9f6c;
  --ink:#1c1f2b;
  --muted:#6b7184;
  --light:#eef1fc;
  --card:#e6eafa;
  --white:#ffffff;
  --line:#d9def0;
  --head:"Oxanium",sans-serif;
  --body:"Cabin",sans-serif;
}
*{box-sizing:border-box;margin:0;padding:0}
html,body{width:1200px;height:5367px;overflow:hidden}
body{position:relative;background:var(--white);font-family:var(--body);color:var(--ink)}
.abs{position:absolute}
h1,h2,h3,.display{font-family:var(--head);font-weight:600;letter-spacing:.2px}
p{line-height:1.45}
a{color:inherit}
.btn{position:absolute;display:flex;align-items:center;justify-content:center;border-radius:6px;font-size:10px;font-weight:700;letter-spacing:.4px;text-transform:uppercase;text-decoration:none}
.btn-green{background:var(--green);color:#fff}
.btn-outline{border:1.5px solid var(--blue);color:var(--blue);background:#fff}
.btn-ghost{border:1.5px solid #fff;color:#fff}
.watermark{position:absolute;left:-20px;font-family:var(--body);font-weight:700;font-size:330px;line-height:1;letter-spacing:2px;color:rgba(47,98,230,.07);white-space:nowrap}

.hero-bg{left:0;top:0;width:1200px;height:710px;background:linear-gradient(180deg,#e9edfb,#eef1fc)}
.nav{left:112px;top:25px;width:976px;height:56px;background:#fff;border-radius:8px;box-shadow:0 4px 14px rgba(40,60,140,.06)}
.nav-links{position:absolute;top:0;height:56px;display:flex;align-items:center;gap:26px;font-size:10px;color:#3b4157}
.wordmark{font-family:var(--body);font-weight:600;color:var(--ink);white-space:nowrap}

.hero-title{left:112px;top:196px;width:540px;font-size:41px;line-height:1.38;color:var(--ink)}
.hero-text{left:112px;top:378px;width:510px;font-size:12.5px;color:#555b70}

.about{left:112px;top:708px;width:976px;height:386px;background:#fff;border-radius:24px;box-shadow:0 10px 30px rgba(40,60,140,.1)}
.mini-card{position:absolute;border-radius:20px;padding:38px 34px}
.mini-card h3{font-size:21px;line-height:1.38}
.mini-card p{font-size:10px;margin-top:12px}

.section-title{width:1200px;left:0;text-align:center;font-size:30px;line-height:1.4}
.feature{position:absolute;border-radius:22px;overflow:hidden}
.feature h3{font-size:21px;line-height:1.4}
.feature p{font-size:10.5px;margin-top:8px}
.feature .more{display:inline-block;font-size:10.5px;font-weight:700;text-decoration:underline;margin-top:8px}
.panel{position:absolute;background:#fff;border-radius:10px;box-shadow:0 6px 20px rgba(20,40,110,.12)}

.faq{left:0;top:2375px;width:1200px;height:535px;background:radial-gradient(circle at 14% 60%,rgba(255,255,255,.08) 0,transparent 30%),radial-gradient(circle at 85% 30%,rgba(255,255,255,.06) 0,transparent 35%),var(--blue)}
.faq-q{position:absolute;left:600px;width:488px;height:40px;border-radius:20px;background:rgba(255,255,255,.88);display:flex;align-items:center;padding-left:18px;font-size:11px;color:#2b3148}
.faq-q .chk{position:absolute;right:6px;top:5px;width:30px;height:30px;border-radius:50%;background:var(--green);display:flex;align-items:center;justify-content:center}

.plan{position:absolute;top:3100px;width:316px;height:212px;border-radius:20px;padding:44px 32px}
.plan h3{font-size:17px}
.plan p{font-size:10px;margin-top:12px;width:190px}
.plan .price{position:absolute;left:32px;font-family:var(--head);font-weight:600;font-size:20px;line-height:1.35}
.plan .go{position:absolute;right:30px;width:32px;height:32px;border-radius:50%;display:flex;align-items:center;justify-content:center}

.testi{left:0;top:3698px;width:1200px;height:521px;background:var(--green)}
.quote-card{position:absolute;top:3868px;width:316px;height:261px;background:#fff;border-radius:20px;padding:26px 26px}
.avatar{position:absolute;left:26px;top:24px;width:82px;height:72px;border-radius:8px;background:linear-gradient(160deg,#c9b7a6,#5b4e48)}
.quote-card .who{position:absolute;left:124px;top:40px}
.quote-card .who b{font-family:var(--head);font-weight:600;font-size:17px;display:block}
.quote-card .who span{font-size:11px;color:var(--muted)}
.quote-card .qm{position:absolute;right:24px;top:28px}
.quote-card .body{position:absolute;left:26px;top:118px;width:262px;font-size:11px;line-height:1.42}
.quote-card .date{position:absolute;left:26px;top:216px;font-size:10.5px;color:var(--blue)}

.blog{position:absolute;top:4375px;width:480px;height:245px;background:var(--card);border-radius:22px;padding:42px 36px}
.blog h3{font-size:18px}
.blog .by{font-size:10px;margin-top:12px;color:#3a4058}
.blog .meta{font-size:10px;margin-top:6px;color:var(--blue)}
.blog p{font-size:10px;color:var(--muted);margin-top:16px}
.blog .more{display:block;font-size:10.5px;color:var(--green);text-decoration:underline;margin-top:20px}

.news{left:112px;top:4775px;width:976px;height:252px;background:var(--blue);border-radius:30px}
.footer-links{left:0;top:5192px;width:1200px;display:flex;justify-content:center;gap:28px;font-size:11px;color:#3a4058}
.social{position:absolute;top:5249px;width:24px;height:24px;border-radius:50%;background:var(--green)}
</style>
</head>
<body>

<div class="abs hero-bg"></div>
<div class="watermark" style="top:510px">Talvora</div>

<nav class="abs nav" aria-label="Main">
  <div class="nav-links" style="left:40px"><span>Features</span><span>FAQ</span><span>About Us</span><span>Pricing</span><span>Blog</span></div>
  <div class="abs wordmark" style="left:0;top:12px;width:976px;text-align:center;font-size:26px;line-height:32px">Talvora</div>
  <div class="nav-links" style="left:684px;gap:22px"><span>Testimonials</span><span>Contact Us</span>
    <svg width="12" height="12" viewBox="0 0 12 12"><circle cx="5" cy="5" r="3.6" fill="none" stroke="#3b4157" stroke-width="1.3"/><path d="M8 8l3 3" stroke="#3b4157" stroke-width="1.3"/></svg></div>
  <div class="btn" style="left:876px;top:8px;width:92px;height:40px;background:var(--blue);color:#fff;border-radius:6px">Log in</div>
</nav>

<h1 class="abs hero-title">Participant management made simple for courses &amp; events.</h1>
<p class="abs hero-text">Create events, take payments, automate emails, and track every participant in one GDPR-compliant system.</p>
<a class="btn btn-green" style="left:112px;top:434px;width:114px;height:38px">Book a demo</a>
<a class="btn btn-outline" style="left:266px;top:434px;width:146px;height:38px">See pricing</a>

<div class="panel" style="left:742px;top:162px;width:346px;height:344px">
  <svg class="abs" style="left:0;top:0" width="346" height="344" viewBox="0 0 346 344">
    <g font-family="Cabin" font-size="6" fill="#8a90a6">
      <rect x="16" y="14" width="38" height="10" rx="3" fill="#eef1fc"/><text x="26" y="21" fill="#2f62e6">Home</text>
      <text x="70" y="21">Users</text><text x="110" y="21">Profile</text><text x="150" y="21">Settings</text>
    </g>
    <g stroke="#eef0f6"><path d="M30 58h160M30 86h160M30 114h160M30 142h160"/></g>
    <path d="M30 135 C60 120 70 80 95 70 S130 120 150 100 S180 70 190 88" fill="none" stroke="#7aa3f7" stroke-width="2"/>
    <path d="M30 135 C60 120 70 80 95 70 S130 120 150 100 S180 70 190 88 V150 H30Z" fill="#2f62e6" opacity=".06"/>
    <text x="88" y="66" font-family="Cabin" font-size="8" fill="#2f62e6">$451</text>
    <rect x="212" y="40" width="120" height="44" rx="6" fill="#f6f8fe"/>
    <text x="222" y="54" font-family="Cabin" font-size="6" fill="#8a90a6">Total revenue</text>
    <text x="222" y="66" font-family="Cabin" font-size="9" fill="#2f62e6">$451</text>
    <path d="M270 70 C285 55 295 68 325 50" fill="none" stroke="#7aa3f7" stroke-width="1.5"/>
    <rect x="212" y="112" width="10" height="10" rx="2" fill="#dfe6fb"/><text x="228" y="119" font-family="Cabin" font-size="6" fill="#3a4058">Ingrid Solberg</text><rect x="310" y="113" width="22" height="7" rx="3" fill="#c9f0de"/>
    <rect x="212" y="140" width="10" height="10" rx="2" fill="#dfe6fb"/><text x="228" y="147" font-family="Cabin" font-size="6" fill="#3a4058">Mats Ekholm</text><rect x="310" y="141" width="22" height="7" rx="3" fill="#fde3c8"/>
    <rect x="168" y="188" width="82" height="62" rx="6" fill="#fff" stroke="#eef0f6"/>
    <path d="M176 228 l10 -8 10 10 10 -14 12 6 16 -10" fill="none" stroke="#f5b55a" stroke-width="1.5"/>
    <rect x="168" y="262" width="82" height="62" rx="6" fill="#fff" stroke="#eef0f6"/>
    <path d="M176 300 l12 6 12 -10 12 8 12 -12 10 4" fill="none" stroke="#17b07b" stroke-width="1.5"/>
    <rect x="262" y="188" width="72" height="136" rx="6" fill="#fff" stroke="#eef0f6"/>
    <g stroke="#2f62e6" stroke-width="2"><path d="M276 310v-30M288 310v-50M300 310v-20M312 310v-60M324 310v-36"/></g>
  </svg>
</div>
<div class="panel" style="left:700px;top:318px;width:160px;height:204px">
  <div class="abs" style="left:56px;top:20px;width:48px;height:48px;border-radius:50%;background:#e3eafc;display:flex;align-items:center;justify-content:center;color:var(--blue);font-size:18px">K</div>
  <div class="abs" style="left:0;top:78px;width:160px;text-align:center;font-size:11px;color:#3a4058">Ingrid Solberg</div>
  <div class="abs" style="left:0;top:94px;width:160px;text-align:center;font-size:7px;color:#8a90a6">Developer</div>
  <div class="abs" style="left:52px;top:110px;width:56px;height:14px;border:1px solid var(--blue);border-radius:4px;font-size:7px;color:var(--blue);text-align:center;line-height:12px">Contact</div>
  <div class="abs" style="left:18px;top:152px;font-size:11px;color:var(--blue)">13 &nbsp; $21k &nbsp; <span style="color:var(--green)">★★★☆</span></div>
</div>

<section class="abs about" aria-labelledby="about-h">
  <h2 id="about-h" class="abs" style="left:59px;top:40px;font-size:29px">About Talvora</h2>
  <p class="abs" style="left:404px;top:40px;width:490px;font-size:10px;color:#555b70">From event planning to follow-up, Plomvik helps you with all the tasks involved in creating a successful event. The so-important participant registration and payment are easily managed by our well-proven system. A new thing is free to publish events in it in our large event catalog.</p>
  <div class="mini-card" style="left:19px;top:130px;width:463px;height:237px;background:var(--card)">
    <h3>Our history</h3>
    <p style="color:#606679;width:360px">For 20 years, we have delivered software to help businesses run their business. Plomvik has been developed based on customers' wishes and needs. It is important to us that the system works for both large and small organizers. Whether you organize competitions, trainings or sell tickets to a theater, we have a system that suits you.</p>
    <a class="btn btn-green" style="left:34px;top:158px;width:140px;height:34px">Leran more</a>
  </div>
  <div class="mini-card" style="left:494px;top:130px;width:463px;height:237px;background:linear-gradient(135deg,var(--green),var(--green-deep));color:#fff">
    <h3>Fundraising &amp; event<br>hosting made easy</h3>
    <p style="width:340px">Plomvik is a comprehensive event listing for marketing &amp; administration, that perfectly aligns events with their audiences.</p>
    <a class="btn btn-ghost" style="left:34px;top:158px;width:140px;height:34px">Get started</a>
  </div>
</section>

<h2 class="abs section-title" style="top:1170px">Powerful features to streamline<br>your events</h2>
<p class="abs" style="left:390px;top:1266px;width:420px;text-align:center;font-size:10.5px;color:#555b70">Everything you need to manage registrations, payments, and communications – all in one platform.</p>

<div class="feature" style="left:112px;top:1340px;width:478px;height:337px;background:linear-gradient(135deg,#2a5ee6,#3d6ff0)">
  <div class="panel" style="left:0;top:28px;width:207px;height:280px;border-radius:0 10px 10px 0">
    <svg width="207" height="280" viewBox="0 0 207 280">
      <rect x="8" y="8" width="80" height="60" rx="4" fill="#f5f7fd"/><path d="M14 40 l12 -10 12 8 14 -14 14 10 12 -6" fill="none" stroke="#2f62e6" stroke-width="1.4"/>
      <rect x="8" y="78" width="80" height="70" rx="4" fill="#f5f7fd"/>
      <g fill="#2f62e6"><rect x="20" y="120" width="7" height="20"/><rect x="32" y="108" width="7" height="32"/><rect x="44" y="114" width="7" height="26"/></g><rect x="56" y="100" width="7" height="40" fill="#f24f5a"/><rect x="68" y="122" width="7" height="18" fill="#17b07b"/>
      <rect x="8" y="158" width="80" height="112" rx="4" fill="#f5f7fd"/>
      <g stroke-width="4"><path d="M16 178h50" stroke="#f5b55a"/><path d="M16 192h40" stroke="#17b07b"/><path d="M16 206h56" stroke="#f24f5a"/><path d="M16 220h34" stroke="#f5b55a"/><path d="M16 234h46" stroke="#2f62e6"/></g>
      <rect x="96" y="8" width="104" height="264" rx="4" fill="#fff" stroke="#eef0f6"/>
      <g stroke="#f0f2f8"><path d="M104 34h88M104 48h88M104 62h88M104 76h88"/></g>
      <g fill="#f5a33a"><circle cx="186" cy="34" r="3"/><circle cx="186" cy="48" r="3"/><circle cx="186" cy="62" r="3"/><circle cx="186" cy="76" r="3"/></g>
      <g stroke="#2f62e6" stroke-width="2"><path d="M110 180v-40M122 180v-24M134 180v-50M146 180v-30M158 180v-44M170 180v-20M182 180v-36"/></g>
      <circle cx="128" cy="240" r="16" fill="none" stroke="#e6eafa" stroke-width="5"/><path d="M128 224 a16 16 0 0 1 0 32" fill="none" stroke="#17b07b" stroke-width="5"/>
    </svg>
  </div>
  <div class="abs" style="left:236px;top:78px;width:220px;color:#fff">
    <h3>Manage your<br>courses</h3>
    <p>Lorem ipsum dolor sit amet, consectetur adipiscing elit, sed do eiusmod tempor incididunt ut labore et dolore magna aliqua. Quis ipsum suspendisse ultrices gravida.</p>
    <a class="more">Learn More</a>
  </div>
</div>

<div class="feature" style="left:606px;top:1340px;width:479px;height:337px;background:var(--card)">
  <div class="panel" style="left:60px;top:0;width:356px;height:162px;border-radius:0 0 10px 10px">
    <svg width="356" height="162" viewBox="0 0 356 162">
      <g font-family="Cabin" font-size="6" fill="#8a90a6"><text x="46" y="10">Jan</text><text x="76" y="10" fill="#2f62e6">Feb</text><text x="106" y="10">Mar</text><text x="136" y="10">Apr</text><text x="166" y="10">May</text><text x="196" y="10">Jun</text></g>
      <rect x="14" y="22" width="96" height="128" rx="6" fill="#fff" stroke="#eef0f6"/>
      <circle cx="62" cy="52" r="14" fill="#e3eafc"/><text x="58" y="56" font-size="10" fill="#2f62e6" font-family="Cabin">K</text>
      <text x="30" y="84" font-size="7" fill="#3a4058" font-family="Cabin">Ingrid Solberg</text>
      <rect x="44" y="94" width="36" height="10" rx="3" fill="none" stroke="#2f62e6"/>
      <text x="26" y="136" font-size="7" fill="#2f62e6" font-family="Cabin">13 · $21k · ★★★</text>
      <rect x="122" y="22" width="110" height="58" rx="6" fill="#fff" stroke="#eef0f6"/><path d="M130 60 l14 -10 14 12 16 -16 14 8 16 -10" fill="none" stroke="#f5b55a" stroke-width="1.5"/>
      <rect x="122" y="92" width="110" height="58" rx="6" fill="#fff" stroke="#eef0f6"/><path d="M130 130 l16 6 14 -10 16 8 16 -12 12 4" fill="none" stroke="#17b07b" stroke-width="1.5"/>
      <rect x="244" y="22" width="96" height="128" rx="6" fill="#fff" stroke="#eef0f6"/>
      <g stroke="#2f62e6" stroke-width="2"><path d="M262 140v-30M276 140v-50M290 140v-20M304 140v-60M318 140v-36"/></g>
    </svg>
  </div>
  <div class="abs" style="left:42px;top:192px;width:360px">
    <h3>Manage your participants</h3>
    <p style="color:#606679">Lorem ipsum dolor sit amet, consectetur adipiscing elit, sed do eiusmod tempor incididunt ut labore et dolore magna aliqua. Quis ipsum suspendisse ultrices gravida. Risus commodo viverra maecenas.</p>
    <a class="more" style="color:var(--blue)">Learn More</a>
  </div>
</div>

<div class="feature" style="left:112px;top:1694px;width:973px;height:270px;background:linear-gradient(135deg,var(--green),var(--green-deep))">
  <div class="abs" style="left:38px;top:82px;width:370px;color:#fff">
    <h3>Manage your payments</h3>
    <p>Lorem ipsum dolor sit amet, consectetur adipiscing elit, sed do eiusmod tempor incididunt ut labore et dolore magna aliqua. Quis ipsum suspendisse ultrices gravida.</p>
    <a class="more">Learn More</a>
  </div>
  <div class="panel" style="left:492px;top:52px;width:448px;height:240px;overflow:hidden">
    <svg width="448" height="240" viewBox="0 0 448 240">
      <rect width="90" height="240" fill="#58627e"/>
      <text x="12" y="14" font-size="6" fill="#fff" font-family="Cabin">DASHBOARD</text>
      <g fill="#aeb6cc"><circle cx="14" cy="38" r="2"/><circle cx="14" cy="50" r="2"/><circle cx="14" cy="62" r="2"/><circle cx="14" cy="74" r="2"/><circle cx="14" cy="86" r="2"/><circle cx="14" cy="98" r="2"/></g>
      <g stroke="#7c86a3" stroke-width="3"><path d="M22 38h30M22 50h26M22 62h34M22 74h22M22 86h28M22 98h20M12 150h60M12 162h54M12 174h62M12 186h48"/></g>
      <rect x="100" y="40" width="220" height="100" rx="4" fill="#fff" stroke="#eef0f6"/>
      <path d="M110 120 l30 -30 30 14 30 -24 30 16 30 -28 30 10" fill="none" stroke="#f5b55a" stroke-width="1.6"/>
      <path d="M110 124 l30 -14 30 8 30 -30 30 24 30 -10 30 6" fill="none" stroke="#2f62e6" stroke-width="1.2" opacity=".6"/>
      <rect x="330" y="40" width="110" height="82" rx="4" fill="#fff" stroke="#eef0f6"/>
      <path d="M338 100 l20 -20 20 10 20 -16 20 8" fill="none" stroke="#f24f5a" stroke-width="1.4"/>
      <rect x="100" y="148" width="64" height="44" rx="4" fill="#fff" stroke="#eef0f6"/><text x="108" y="174" font-size="9" fill="#2f62e6" font-family="Cabin">$ 2723</text>
      <rect x="178" y="148" width="64" height="44" rx="4" fill="#fff" stroke="#eef0f6"/><text x="184" y="174" font-size="9" fill="#f5a33a" font-family="Cabin">$ 143,000</text>
      <rect x="256" y="148" width="64" height="44" rx="4" fill="#fff" stroke="#eef0f6"/><text x="262" y="174" font-size="9" fill="#17b07b" font-family="Cabin">$ 32,000</text>
      <rect x="330" y="130" width="110" height="100" rx="4" fill="#fff" stroke="#eef0f6"/>
      <g stroke="#eef0f6"><path d="M338 150h94M338 164h94M338 178h94M338 192h94"/></g>
      <g stroke-width="4"><path d="M200 232v-18" stroke="#2f62e6"/><path d="M210 232v-10" stroke="#17b07b"/><path d="M220 232v-22" stroke="#f24f5a"/></g>
    </svg>
  </div>
</div>

<div class="watermark" style="top:2010px">Talvora</div>

<section class="abs faq" aria-labelledby="faq-h"></section>
<h2 id="faq-h" class="abs section-title" style="top:2446px;color:#fff">Frequently asked questions</h2>
<p class="abs" style="left:0;top:2500px;width:1200px;text-align:center;font-size:10px;color:#fff">Answers to common questions about using Talvora.</p>
<div class="abs" style="left:112px;top:2573px;width:396px;height:219px;background:#fff;border-radius:22px;padding:38px 32px">
  <h3 style="font-family:var(--body);font-weight:700;font-size:17px">Your Question is not in this FAQ?</h3>
  <p style="font-size:9.5px;color:#7a8093;margin-top:10px;width:300px">Lorem ipsum dolor sit amet, consectetur adipiscing elit, sed do eiusmod tempor incididunt ut labore et dolore magna aliqua. Quis ipsum suspendisse ultrices gravida. Risus commodo viverra.</p>
  <a class="btn btn-green" style="left:32px;top:134px;width:164px;height:32px;font-size:9px">Free consultation</a>
  <a class="btn btn-outline" style="left:209px;top:134px;width:146px;height:32px;font-size:9px">Full simulator</a>
</div>
<div class="faq-q" style="top:2577px">How does Talvora handle payments?<span class="chk"><svg width="14" height="14" viewBox="0 0 14 14"><path d="M3 5.5l4 4 4-4" fill="none" stroke="#fff" stroke-width="2"/></svg></span></div>
<div class="faq-q" style="top:2635px">Can I customize registration fields?<span class="chk"><svg width="14" height="14" viewBox="0 0 14 14"><path d="M3 5.5l4 4 4-4" fill="none" stroke="#fff" stroke-width="2"/></svg></span></div>
<div class="faq-q" style="top:2693px">Is Talvora GDPR compliant?<span class="chk"><svg width="14" height="14" viewBox="0 0 14 14"><path d="M3 5.5l4 4 4-4" fill="none" stroke="#fff" stroke-width="2"/></svg></span></div>
<div class="faq-q" style="top:2752px">Does Talvora integrate with our website?<span class="chk"><svg width="14" height="14" viewBox="0 0 14 14"><path d="M3 5.5l4 4 4-4" fill="none" stroke="#fff" stroke-width="2"/></svg></span></div>

<h2 class="abs section-title" style="top:3003px">Pick a plan. Grow faster with Plomvik.</h2>
<div class="plan" style="left:112px;background:#fff;border:2px solid #8fd9bd">
  <h3>Essential</h3><p style="color:#606679">Start receiving payments and registrations instantly</p>
  <div class="price" style="top:146px;font-size:18px">Free</div>
  <div class="go" style="top:140px;background:var(--blue)"><svg width="12" height="12" viewBox="0 0 12 12"><path d="M4 2l4 4-4 4" fill="none" stroke="#fff" stroke-width="1.8"/></svg></div>
</div>
<div class="plan" style="left:444px;background:var(--card)">
  <h3>Standard</h3><p style="color:#606679">Integrate forms to your own site and make clients stay</p>
  <div class="price" style="top:128px">$0.5 per<br>registration*</div>
  <div class="go" style="top:140px;background:var(--green)"><svg width="12" height="12" viewBox="0 0 12 12"><path d="M4 2l4 4-4 4" fill="none" stroke="#fff" stroke-width="1.8"/></svg></div>
</div>
<div class="plan" style="left:771px;background:linear-gradient(135deg,var(--green),var(--green-deep));color:#fff">
  <h3>Premium</h3><p>Unlock all features and get your own branding</p>
  <div class="price" style="top:128px;font-size:19px">$25 per month+<br>$0.5 per registration*</div>
  <div class="go" style="top:140px;background:#fff"><svg width="12" height="12" viewBox="0 0 12 12"><path d="M4 2l4 4-4 4" fill="none" stroke="#17b07b" stroke-width="1.8"/></svg></div>
</div>

<div class="watermark" style="top:3340px">Talvora</div>

<section class="abs testi" aria-labelledby="testi-h"></section>
<h2 id="testi-h" class="abs" style="left:100px;top:3770px;font-size:30px;color:#fff">What our clients say</h2>
<p class="abs" style="left:671px;top:3776px;width:420px;font-size:11px;color:#fff">Lorem ipsum dolor sit amet, consectetur adipiscing elit, sed do eiusmod tempor incididunt ut labore et dolore magna aliqua.</p>

<article class="quote-card" style="left:112px">
  <div class="avatar" role="img" aria-label="Portrait photo of client"></div>
  <div class="who"><b>Joel M.</b><span>Designer</span></div>
  <svg class="qm" width="50" height="40" viewBox="0 0 50 40"><path d="M2 2h20v22l-8 14H6l6-14H2zM28 2h20v22l-8 14h-8l6-14h-10z" fill="#c4c8d4"/></svg>
  <p class="body">Lorem ipsum dolor sit amet, consectetur adipiscing elit, sed do eiusmod tempor incididunt ut labore et dolore magna aliqua. Quis ipsum suspendisse ultrices gravida.</p>
  <span class="date">15 May 2025 6:30 am</span>
</article>
<article class="quote-card" style="left:442px">
  <div class="avatar" role="img" aria-label="Portrait photo of client" style="background:linear-gradient(160deg,#d9cfc3,#7a6c5f)"></div>
  <div class="who"><b>Joel M.</b><span>Designer</span></div>
  <svg class="qm" width="50" height="40" viewBox="0 0 50 40"><path d="M2 2h20v22l-8 14H6l6-14H2zM28 2h20v22l-8 14h-8l6-14h-10z" fill="#c4c8d4"/></svg>
  <p class="body">Lorem ipsum dolor sit amet, consectetur adipiscing elit, sed do eiusmod tempor incididunt ut labore et dolore magna aliqua. Quis ipsum suspendisse ultrices gravida.</p>
  <span class="date">15 May 2025 6:30 am</span>
</article>
<article class="quote-card" style="left:771px">
  <div class="avatar" role="img" aria-label="Portrait photo of client" style="background:linear-gradient(160deg,#c9a79c,#8c3f3a)"></div>
  <div class="who"><b>Joel M.</b><span>Designer</span></div>
  <svg class="qm" width="50" height="40" viewBox="0 0 50 40"><path d="M2 2h20v22l-8 14H6l6-14H2zM28 2h20v22l-8 14h-8l6-14h-10z" fill="#c4c8d4"/></svg>
  <p class="body">Lorem ipsum dolor sit amet, consectetur adipiscing elit, sed do eiusmod tempor incididunt ut labore et dolore magna aliqua. Quis ipsum suspendisse ultrices gravida.</p>
  <span class="date">15 May 2025 6:30 am</span>
</article>

<h2 class="abs section-title" style="top:4300px">Latest blogs</h2>
<article class="blog" style="left:112px">
  <h3>Quis ipsum suspendisse ultrices gravida.</h3>
  <div class="by">by Henrik L. Dahl</div>
  <div class="meta">15 Dec 2021 - Less than 1 minute read</div>
  <p>Lorem ipsum dolor sit amet, consectetur adipiscing elit, sed do eiusmod tempor incididunt ut labore et dolore magna aliqua. Quis ipsum suspendisse ultrices gravida. Risus commodo viverra maecenas accumsan lacus vel facilisis.</p>
  <a class="more">Read More</a>
</article>
<article class="blog" style="left:606px">
  <h3>Quis ipsum suspendisse ultrices gravida.</h3>
  <div class="by">by Henrik L. Dahl</div>
  <div class="meta">15 Dec 2021 - Less than 1 minute read</div>
  <p>Lorem ipsum dolor sit amet, consectetur adipiscing elit, sed do eiusmod tempor incididunt ut labore et dolore magna aliqua. Quis ipsum suspendisse ultrices gravida. Risus commodo viverra maecenas accumsan lacus vel facilisis.</p>
  <a class="more">Read More</a>
</article>
<a class="btn btn-green" style="left:531px;top:4646px;width:140px;height:32px;font-size:9px">View more</a>

<section class="abs news" aria-labelledby="news-h">
  <h2 id="news-h" class="abs" style="left:71px;top:62px;font-size:30px;line-height:1.35;color:#fff">Subscribe to our<br>newsletter</h2>
  <p class="abs" style="left:71px;top:160px;font-size:10px;color:#fff">Subscribe now to get the latest news and updates at the earliest.</p>
  <div class="abs" style="left:498px;top:82px;width:340px;height:34px;border:1.5px solid rgba(255,255,255,.8);border-radius:8px;font-size:10px;color:#fff;padding:10px 18px">Enter Email</div>
  <a class="btn btn-green" style="left:498px;top:138px;width:152px;height:32px;font-size:9px">Subscribe</a>
</section>

<div class="abs wordmark" style="left:0;top:5104px;width:1200px;text-align:center;font-size:44px;line-height:54px">Talvora</div>
<nav class="abs footer-links" aria-label="Footer"><span>Features</span><span>FAQ</span><span>About Us</span><span>Pricing</span><span>Blog</span><span>Testimonials</span><span>Contact Us</span></nav>
<div class="abs" style="left:112px;top:5261px;width:400px;height:1px;background:var(--line)"></div>
<div class="abs" style="left:688px;top:5261px;width:400px;height:1px;background:var(--line)"></div>
<span class="social" style="left:526px" role="img" aria-label="Social profile"></span>
<span class="social" style="left:566px" role="img" aria-label="Social profile"></span>
<span class="social" style="left:606px" role="img" aria-label="Social profile"></span>
<span class="social" style="left:646px" role="img" aria-label="Social profile"></span>
<p class="abs" style="left:0;top:5306px;width:1200px;text-align:center;font-size:9.5px;color:#3a4058">Copyright © 2025. All rights reserved</p>

</body>
</html>
```